Business Card Design for Concierge business

Hi. I would like to have an elegant, smart business card for my concierge business, called Harbor Concierge. The services I provide are mail management, dog walking, cleaning, car, stylist, personal shopper, running errands, property management, event planning. I was thinking to add my picture but I would like to see options without it as well, if possible.

Thank you.

Business Card Details:
*Designers are to solely use contact information for the business card design. This is not to be used to contact the customer*

Name: Mirela Dobos
mail: tidewayconcierge@mailvista.example
Phone: 555-284-1097

Target Market(s)

vacation home owners

Industry/Entity Type

Business

Font styles to use
Serif

Colors

Designer to choose colors to be used in the design.

Requirements
Nice to have
• Could use icons that describe the services I provide for example car, house, key, shopping cart, shopping bags, envelope, champagne glasses, phone, dog etc.

```html
<!DOCTYPE html>
<html lang="en">
<head>
<meta charset="utf-8">
<title>Harbor Concierge – Business Card</title>
<link href="https://fonts.googleapis.com/css2?family=Playfair+Display:ital,wght@1,700&family=Open+Sans:wght@400;600&family=Montserrat:wght@700&display=swap" rel="stylesheet">
<style>
  :root {
    --stage: #0f0f0f;
    --card-black: #1a1a1a;
    --sand: #b89a76;
    --sand-light: #d9c3a0;
    --gold-text: #e8c596;
    --ink: #141414;
    --white: #ffffff;
    --orange: #f6ad3c;
    --purple: #3f2a66;
    --navy: #262a5a;
    --green: #1f9e4e;
  }
  * { margin: 0; padding: 0; box-sizing: border-box; }
  html, body { width: 1200px; height: 1000px; overflow: hidden; }
  body { background: var(--stage); position: relative; }

  .card {
    position: absolute;
    top: 350px;
    width: 520px;
    height: 300px;
    border-radius: 22px;
    overflow: hidden;
  }
  .card--front { left: 60px; background: var(--card-black); }
  .card--back { left: 620px; background: var(--white); }

  .card-art { position: absolute; inset: 0; }

  .owner-name {
    position: absolute;
    right: 34px;
    top: 92px;
    font-family: "Playfair Display", serif;
    font-style: italic;
    font-weight: 700;
    font-size: 30px;
    color: var(--gold-text);
  }
  .contact {
    position: absolute;
    right: 30px;
    bottom: 26px;
    text-align: right;
    font-family: "Open Sans", sans-serif;
    font-size: 15px;
    line-height: 1.3;
    color: var(--ink);
  }

  .service {
    position: absolute;
    font-family: "Montserrat", sans-serif;
    font-weight: 700;
    font-size: 9.5px;
    letter-spacing: 0.06em;
    text-transform: uppercase;
    color: var(--ink);
    white-space: nowrap;
  }
  .icon { position: absolute; }
</style>
</head>
<body>

<section class="card card--front">
  <svg class="card-art" width="520" height="300" viewBox="0 0 520 300">
    <defs>
      <linearGradient id="portraitTone" x1="0" y1="0" x2="1" y2="1">
        <stop offset="0" stop-color="#cdb593"/>
        <stop offset="0.6" stop-color="#a8916f"/>
        <stop offset="1" stop-color="#6e5f4c"/>
      </linearGradient>
    </defs>
    <rect class="portrait" x="0" y="0" width="300" height="300" fill="url(#portraitTone)" role="img" aria-label="Portrait photo of the concierge"/>
    <path class="panel-dark" d="M300 0 H520 V300 H140 C200 250 235 200 250 140 C262 90 275 40 300 0 Z" fill="var(--card-black)"/>
    <path class="panel-sand" d="M150 300 C190 230 270 185 370 185 C440 185 495 205 520 225 V300 Z" fill="var(--sand)"/>
  </svg>
  <h1 class="owner-name">Mirela Dobos</h1>
  <p class="contact">555-284-1097<br>tidewayconcierge@mailvista.example</p>
</section>

<section class="card card--back">
  <span class="service" style="left:26px;top:22px">Property Management</span>
  <svg class="icon" style="left:34px;top:40px" width="30" height="26" viewBox="0 0 30 26">
    <path d="M15 1 L29 13 H25 V25 H18 V17 H12 V25 H5 V13 H1 Z" fill="var(--green)"/>
  </svg>

  <span class="service" style="left:262px;top:70px">Stylist</span>
  <svg class="icon" style="left:262px;top:86px" width="40" height="18" viewBox="0 0 40 18">
    <rect x="2" y="2" width="36" height="6" rx="2" fill="var(--ink)"/>
    <path d="M6 8 V16 M10 8 V16 M14 8 V16 M18 8 V16 M22 8 V16 M26 8 V16 M30 8 V16 M34 8 V16" stroke="var(--ink)" stroke-width="1.6"/>
  </svg>

  <span class="service" style="left:396px;top:106px">Personal Shopper</span>
  <svg class="icon" style="left:446px;top:124px" width="30" height="34" viewBox="0 0 30 34">
    <path d="M10 10 V6 a5 5 0 0 1 10 0 V10" stroke="var(--purple)" stroke-width="2" fill="none"/>
    <rect x="2" y="10" width="26" height="23" rx="2" fill="var(--purple)"/>
  </svg>

  <svg class="icon" style="left:30px;top:82px" width="48" height="48" viewBox="0 0 48 48">
    <circle cx="24" cy="24" r="21" fill="var(--white)" stroke="var(--purple)" stroke-width="2.5"/>
    <rect x="12" y="16" width="24" height="16" rx="2" fill="var(--orange)"/>
    <path d="M12 17 L24 26 L36 17" stroke="var(--white)" stroke-width="1.6" fill="none"/>
  </svg>
  <span class="service" style="left:84px;top:108px">Mail Management</span>

  <svg class="icon" style="left:32px;top:150px" width="36" height="26" viewBox="0 0 36 26">
    <path d="M6 11 L10 3 H26 L30 11 H33 V21 H3 V11 Z" fill="var(--navy)"/>
    <path d="M11 5 H25 L28 11 H8 Z" fill="var(--white)"/>
    <circle cx="9" cy="22" r="3.5" fill="var(--navy)"/>
    <circle cx="27" cy="22" r="3.5" fill="var(--navy)"/>
  </svg>
  <span class="service" style="left:24px;top:186px">Car Cleaning</span>

  <svg class="icon" style="left:218px;top:118px" width="84" height="84" viewBox="0 0 84 84">
    <circle cx="42" cy="42" r="40" fill="var(--orange)"/>
    <circle cx="42" cy="33" r="9" fill="var(--white)"/>
    <path d="M26 58 a16 14 0 0 1 32 0 Z" fill="var(--white)"/>
  </svg>

  <span class="service" style="left:312px;top:182px">Running Errands</span>
  <svg class="icon" style="left:438px;top:172px" width="50" height="50" viewBox="0 0 50 50">
    <circle cx="25" cy="25" r="22" fill="var(--white)" stroke="var(--purple)" stroke-width="2.5"/>
    <rect x="16" y="13" width="18" height="24" rx="1.5" fill="var(--orange)"/>
    <path d="M19 19 H31 M19 23 H31 M19 27 H31 M19 31 H27" stroke="var(--white)" stroke-width="1.5"/>
  </svg>

  <svg class="icon" style="left:226px;top:206px" width="34" height="32" viewBox="0 0 34 32">
    <rect x="3" y="3" width="26" height="26" fill="none" stroke="var(--ink)" stroke-width="2"/>
    <path d="M3 12 H29 M3 20 H29 M12 3 V29 M20 3 V29" stroke="var(--ink)" stroke-width="1.5"/>
    <path d="M8 16 L14 23 L32 5" stroke="var(--green)" stroke-width="3" fill="none"/>
  </svg>
  <span class="service" style="left:188px;top:248px">Event Planning</span>

  <svg class="icon" style="left:448px;top:232px" width="30" height="30" viewBox="0 0 30 30">
    <ellipse cx="6" cy="13" rx="3.2" ry="4" fill="var(--ink)"/>
    <ellipse cx="11.5" cy="6" rx="3.2" ry="4" fill="var(--ink)"/>
    <ellipse cx="18.5" cy="6" rx="3.2" ry="4" fill="var(--ink)"/>
    <ellipse cx="24" cy="13" rx="3.2" ry="4" fill="var(--ink)"/>
    <path d="M15 14 C10 14 6 21 8 25 C10 28 13 26 15 26 C17 26 20 28 22 25 C24 21 20 14 15 14 Z" fill="var(--ink)"/>
  </svg>
  <span class="service" style="left:398px;top:272px">Dog Walking</span>
</section>

</body>
</html>
```